Northern Tempest Informational Sheet

I need a one page informational sheet (advertisement) for a horse called Northern Tempest. It should have the name Northern Tempest and the content below. It needs to be eye-catching. I have attached 3 examples of what these advertisements look like so it's easier to create. I've also attached 2 pictures of the horse which should both be used in the advertisement.

Here are the bullet points:

- Son of Distant Harbor with total progeny earnings over 13 million dollars
- Ranks among West Virginia top 3 active sires by progeny earnings 2019
- In 9 crops of racing age, has sired 200 winners from 275 starters
- Sired Don Marbellino who earned over $800k racing from age 2 to 7.
- Won 3 of 4 lifetime starts

stands at stud for $1000 at Ashgrove Farm near Charles Town
Call Dwight Kessler - (304) 555-0193

Target Market(s)

Thoroughbred racing people interested in breeding

Requirements
Must have
• Unique and creative. The name of the horse Northern Tempest should be clear and bold, the picture should also be prominent.
Should not have
• Cartoon like, whimsical

```html
<!DOCTYPE html>
<html lang="en">
<head>
<meta charset="utf-8">
<title>Northern Tempest – Stallion Sheet</title>
<link href="https://fonts.googleapis.com/css2?family=Josefin+Sans:wght@200;300&family=Fauna+One&family=Lato:wght@700&display=swap" rel="stylesheet">
<style>
  :root {
    --page-bg: #f1f1ef;
    --sheet-bg: #e3e9e8;
    --band-black: #1d1d1f;
    --footer-black: #0c0c0c;
    --panel-grey: #5c6968;
    --text-light: #ffffff;
    --photo-dark: #3a3d3d;
    --photo-mid: #6b6f6e;
    --coat-bay: #8a3a1a;
    --coat-light: #b5552a;
    --door-green: #5f7d72;
  }
  * { margin: 0; padding: 0; box-sizing: border-box; }
  html, body { width: 1200px; height: 1200px; overflow: hidden; }
  body { background: var(--page-bg); position: relative; }

  .sheet {
    position: absolute; left: 207px; top: 45px;
    width: 786px; height: 1110px;
    background: var(--sheet-bg);
  }
  .hero-photo {
    position: absolute; left: 30px; top: 24px; width: 727px; height: 508px;
    background:
      radial-gradient(ellipse 38% 30% at 52% 48%, var(--coat-light) 0%, var(--coat-bay) 55%, transparent 100%),
      linear-gradient(180deg, #8e9392 0%, var(--photo-mid) 45%, var(--photo-dark) 100%);
  }
  .feature {
    position: absolute; left: 30px; top: 538px; width: 727px; height: 421px;
  }
  .feature svg { position: absolute; left: 0; top: 0; }
  .portrait-photo {
    position: absolute; left: 250px; top: 107px; width: 226px; height: 314px;
    background:
      radial-gradient(ellipse 45% 55% at 55% 65%, var(--coat-light) 0%, var(--coat-bay) 60%, transparent 100%),
      linear-gradient(180deg, #c0502c 0%, var(--door-green) 12%, #4d655c 100%);
  }
  .feature-title {
    position: absolute; left: 0; top: 20px; width: 727px;
    text-align: center;
    font-family: "Josefin Sans", sans-serif; font-weight: 200;
    font-size: 44px; letter-spacing: 6px; color: var(--text-light);
    line-height: 48px;
  }
  .facts {
    position: absolute; list-style: none;
    font-family: "Fauna One", serif; font-size: 15.5px; line-height: 19px;
    color: var(--text-light);
  }
  .facts li { position: absolute; left: 0; }
  .facts li::before { content: "\25C6"; font-size: 12px; margin-right: 7px; }
  .facts-left { left: 21px; top: 172px; width: 200px; }
  .facts-right { left: 507px; top: 172px; width: 205px; }
  .facts-left li:nth-child(1) { top: 0; }
  .facts-left li:nth-child(2) { top: 133px; }
  .facts-right li:nth-child(1) { top: 0; }
  .facts-right li:nth-child(2) { top: 76px; }
  .facts-right li:nth-child(3) { top: 152px; }

  .booking {
    position: absolute; left: 30px; top: 967px; width: 727px; height: 116px;
    background: var(--footer-black); color: var(--text-light);
    text-align: center;
  }
  .booking-fee {
    position: absolute; left: 0; width: 100%; top: 19px;
    font-family: "Fauna One", serif; font-size: 17px;
  }
  .booking-contact {
    position: absolute; left: 0; width: 100%; top: 64px;
    font-family: "Fauna One", serif; font-size: 16px;
  }
  .booking-contact strong { font-family: "Lato", sans-serif; font-weight: 700; font-size: 16px; }
</style>
</head>
<body>
  <article class="sheet">
    <div class="hero-photo" role="img" aria-label="Photo of Northern Tempest, a bay stallion standing in profile beside a brick barn"></div>

    <section class="feature">
      <div class="portrait-photo" role="img" aria-label="Front three-quarter photo of Northern Tempest in a halter before a green barn door"></div>
      <svg width="727" height="421" viewBox="0 0 727 421" aria-hidden="true">
        <polygon class="panel-left" points="0,76 241,105 241,421 0,421" fill="var(--panel-grey)"/>
        <polygon class="panel-right" points="485,105 727,76 727,421 485,421" fill="var(--panel-grey)"/>
        <polygon class="title-band" points="0,0 727,0 727,68 368,112 0,68" fill="var(--band-black)" stroke="#ffffff" stroke-width="4"/>
        <rect x="0" y="0" width="727" height="4" fill="var(--band-black)"/>
      </svg>
      <h1 class="feature-title">NORTHERN TEMPEST</h1>
      <ul class="facts facts-left">
        <li>Son of Distant Harbor with total progeny earnings over 13 million dollars</li>
        <li>Ranks among West Virginia top 3 active sires by progeny earnings 2019</li>
      </ul>
      <ul class="facts facts-right">
        <li>In 9 crops of racing age, has sired 200 winners from 275 starters</li>
        <li>Sired Don Marbellino who earned over $800k racing from age 2 to 7.</li>
        <li>Won 3 of 4 lifetime starts.</li>
      </ul>
    </section>

    <footer class="booking">
      <p class="booking-fee">Stands at stud for $1000 at Ashgrove Farm near Charles Town</p>
      <p class="booking-contact"><strong>CALL DWIGHT KESSLER</strong> - (304) 555-0193</p>
    </footer>
  </article>
</body>
</html>
```